Northgate Pension Partners Needs a Fresh Business Card Update!

We are looking forward to a busy year ahead and have just launched our new website. We are looking to you for a fresh update to our business cards!

Here is a link to our website: http://www.northgatepensionpartners.example/

You will find our logo attached in two formats for your use. Our old business card front and back is also attached for your reference. We want to have a portrait space on the new cards similar to the old card that we can interchange with various employee portraits or keep blank.
We are also interested in seeing a play on colors that matches our website and logo.

For the back of the card please make the following changes (from our old card):

1. The new "FREE REPORT" is titled as follows: FREE REPORT - 4 Traps That Empty a Nest Egg

2. Under "How Can We Help You?" please list out the following in place of the longer list:

Determine Retirement Eligibility & Best Date for You to Retire
Organizing Important Documents for Retirement
Calculate your annuity estimate
Completing Retirement Paperwork
Survivor Benefit Options
Deposits and Re-deposits
Military Service
Social Security Questions
CAWP Special Supplement
Health Insurance
Early-Out Options
Larkmoor Deposit Scheme (during service and after retirement)

3. Under: "Am I on Track to Retire?" please edit the sentence to read:
Find out by Scheduling a "FREE" Federal Benefit & Analysis Counseling Session

Designers, Thank you for your creativity!

Target Market(s)

Federal Employees ages 45-65

Industry/Entity Type

Financial Planning

Contact Information for Business Card

We want to have a portrait space on the front of the new cards similar to the old card that we can interchange with various employee portraits or keep blank. The only text that is negotiable on the front of the card is the bulleted text.
We would like for you to use colors that match our website and logo.

Survivor Benefit Options
Deposits and Re-deposits
Military Service
Social Security Questions
CAWP Special Supplement
Health Insurance
Early-Out Options

Font styles to use
Serif

Requirements
Must have
• Colors to match our logo and new website: http://www.northgatepensionpartners.example/

```html
<!DOCTYPE html>
<html lang="en">
<head>
<meta charset="utf-8">
<title>Northgate Pension Partners – Stationery Proof #2</title>
<link href="https://fonts.googleapis.com/css2?family=Montserrat:wght@400;500;600;700&display=swap" rel="stylesheet">
<style>
  :root{
    --navy:#15203a;
    --red:#d42a2a;
    --sky:#7fb0d6;
    --brand-blue:#2b7bc6;
    --panel:#ececec;
    --ink:#222;
    --label:#7a7a7a;
    --board:#e4e2df;
    --white:#ffffff;
  }
  *{box-sizing:border-box;margin:0;padding:0}
  html,body{width:1200px;height:1200px;overflow:hidden}
  body{background:var(--board);font-family:"Montserrat",sans-serif;color:var(--ink);position:relative}
  .section-label{position:absolute;font-size:35px;font-weight:400;color:var(--label);letter-spacing:.5px;line-height:1}
  .piece{position:absolute;background:var(--white);box-shadow:0 2px 6px rgba(0,0,0,.25);overflow:hidden}
  .band{position:absolute;left:0;right:0}
  .navy{background:var(--navy)}
  .center{text-align:center}

  .brand{display:flex;flex-direction:column;align-items:center;gap:6px}
  .brand-mark{border:2px solid var(--white);border-radius:50%;background:transparent}
  .brand-name{color:var(--brand-blue);font-weight:600;text-transform:uppercase;text-align:center;line-height:1.15}

  /* business card front */
  .card-front{left:642px;top:51px;width:230px;height:406px}
  .card-front .band.navy{top:0;height:163px;display:flex;justify-content:center;align-items:center}
  .card-front .brand-mark{width:56px;height:56px}
  .card-front .brand-name{font-size:16px;letter-spacing:.5px}
  .tagline{top:163px;height:50px;background:var(--red);color:var(--white);font-size:8.6px;font-weight:700;letter-spacing:3.2px;line-height:12.5px;padding:6px 0 0 14px}
  .intro{top:213px;height:96px;background:var(--panel);padding-top:12px;font-size:9.3px;line-height:11.6px}
  .person-name{color:var(--red);font-size:14px;font-weight:700;margin-top:6px}
  .person-email{font-size:10.5px;font-weight:600;margin-top:5px}
  .contact{top:309px;bottom:0;background:var(--sky);padding-top:9px;font-size:9.3px;font-weight:600;line-height:11.3px;color:var(--navy)}
  .contact .gap{height:5px}

  /* business card back */
  .card-back{left:902px;top:51px;width:231px;height:406px}
  .card-back .band.navy{top:0;height:107px}
  .card-back .brand{position:absolute;left:14px;top:46px;width:118px}
  .card-back .brand-mark{width:30px;height:30px}
  .card-back .brand-name{font-size:9px}
  .portrait{position:absolute;left:137px;top:16px;width:80px;height:80px;border-radius:50%;border:2px solid var(--white);background:radial-gradient(circle at 50% 40%,#b9b9b9,#5a5a5a)}
  .services{top:107px;height:252px;background:var(--panel);padding-top:10px;font-size:8.9px;font-weight:600;line-height:11.35px;color:var(--navy)}
  .services h3,.services h4{color:var(--red);font-size:10.4px;font-weight:700;letter-spacing:2.6px}
  .services h4{margin-top:10px}
  .back-foot{top:359px;bottom:0;background:var(--sky);color:var(--white);font-size:9.4px;font-weight:600;line-height:12px;padding-top:11px}

  /* stationery headers */
  .stationery-head{display:flex;justify-content:space-between;align-items:center;padding:0 36px 0 34px}
  .stationery-head .brand-mark{width:30px;height:30px}
  .stationery-head .brand-name{font-size:10px;width:130px}
  .head-contact{color:var(--white);font-size:6.4px;font-weight:600;line-height:7.4px;text-align:center}
  .head-contact .gap{height:7px}

  .letterhead{left:67px;top:474px;width:514px;height:664px;background:linear-gradient(#ececec 0%,#fff 35%,#fff 70%,#ebebeb 100%)}
  .letterhead .band.navy{top:0;height:70px}
  .letterhead .foot{bottom:0;height:22px;background:var(--sky)}

  .comp-slip{left:630px;top:557px;width:514px;height:221px}
  .comp-slip .band.navy{top:0;height:70px}
  .comp-rule{top:78px;height:12px;display:flex;align-items:center;gap:8px}
  .comp-rule .line{flex:1;height:1px;background:var(--red)}
  .comp-rule span{color:var(--red);font-size:9.4px;font-weight:700;letter-spacing:2.6px}
  .comp-rule .line.short{flex:0 0 184px}

  .envelope{left:630px;top:882px;width:514px;height:256px}
  .envelope .return{position:absolute;left:14px;top:20px;width:120px;font-size:6.4px;line-height:7.4px;text-align:center}
  .envelope .brand-mark{width:30px;height:30px;border-color:var(--navy)}
  .envelope .brand-name{font-size:10px}
  .envelope .brand{margin-bottom:4px}
</style>
</head>
<body>
  <div class="section-label" style="left:56px;top:58px">PROOF #2</div>
  <div class="section-label" style="left:324px;top:58px">BUSINESS CARD</div>
  <div class="section-label" style="left:68px;top:418px">LETTERHEAD</div>
  <div class="section-label" style="left:632px;top:500px">WITH COMPLIMENTS SLIP</div>
  <div class="section-label" style="left:632px;top:830px">ENVELOPE</div>

  <section class="piece card-front">
    <div class="band navy">
      <div class="brand">
        <div class="brand-mark"></div>
        <div class="brand-name">Northgate Pension<br>Partners</div>
      </div>
    </div>
    <div class="band tagline">INFORMATION YOU NEED<br>ADVICE YOU CAN TRUST<br>SUPPORT YOU CAN COUNT ON</div>
    <div class="band intro center">
      <p>Dedicated to and Specializing<br>in LTRS/CAWP &amp; the Financial Needs<br>of Federal Employees</p>
      <p class="person-name">DANA WHITLOW</p>
      <p class="person-email">dana@danawhitlow.example</p>
    </div>
    <div class="band contact center">
      <p>555-230-0148<br>Toll Free: 1-800-555-0172<br>Fax 1-800-555-0190</p>
      <div class="gap"></div>
      <p>410 Cedar Row, Suite 12<br>Brookfield, ST 00000<br>www.northgatepensionpartners.example</p>
    </div>
  </section>

  <section class="piece card-back">
    <div class="band navy">
      <div class="brand">
        <div class="brand-mark"></div>
        <div class="brand-name">Northgate Pension Partners</div>
      </div>
      <div class="portrait" role="img" aria-label="Employee portrait"></div>
    </div>
    <div class="band services center">
      <h3>HOW CAN WE HELP YOU?</h3>
      <p>Determine Retirement Eligibility &amp;<br>Best Date for You to Retire<br>Organizing Important Documents<br>for Retirement<br>Calculate your annuity estimate<br>Completing Retirement Paperwork<br>Survivor Benefit Options<br>Deposits and Re-deposits<br>Military Service<br>Social Security Questions<br>CAWP Special Supplement<br>Health Insurance<br>Early-Out Options<br>Larkmoor Deposit Scheme<br>(during service and after retirement)</p>
      <h4>AM I ON TRACK TO RETIRE?</h4>
      <p>Find out by Scheduling a “FREE” Federal<br>Benefit &amp; Analysis Counselling Session</p>
    </div>
    <div class="band back-foot center">TOLL FREE: 1-800-555-0172<br>www.northgatepensionpartners.example</div>
  </section>

  <section class="piece letterhead">
    <div class="band navy stationery-head">
      <div class="brand">
        <div class="brand-mark"></div>
        <div class="brand-name">Northgate Pension Partners</div>
      </div>
      <div class="head-contact">
        <p>555-230-0148<br>Toll Free: 1-800-555-0172<br>Fax 1-800-555-0190</p>
        <div class="gap"></div>
        <p>410 Cedar Row, Suite 12 Brookfield, ST 00000<br>www.northgatepensionpartners.example</p>
      </div>
    </div>
    <div class="band foot"></div>
  </section>

  <section class="piece comp-slip">
    <div class="band navy stationery-head">
      <div class="brand">
        <div class="brand-mark"></div>
        <div class="brand-name">Northgate Pension Partners</div>
      </div>
      <div class="head-contact">
        <p>555-230-0148<br>Toll Free: 1-800-555-0172<br>Fax 1-800-555-0190</p>
        <div class="gap"></div>
        <p>410 Cedar Row, Suite 12 Brookfield, ST 00000<br>www.northgatepensionpartners.example</p>
      </div>
    </div>
    <div class="band comp-rule">
      <div class="line short"></div><span>WITH COMPLIMENTS</span><div class="line"></div>
    </div>
  </section>

  <section class="piece envelope">
    <div class="return">
      <div class="brand">
        <div class="brand-mark"></div>
        <div class="brand-name">Northgate Pension Partners</div>
      </div>
      <p>555-230-0148<br>Toll Free: 1-800-555-0172<br>Fax 1-800-555-0190<br>410 Cedar Row, Suite 12<br>Brookfield, ST 00000<br>www.northgatepensionpartners.example</p>
    </div>
  </section>
</body>
</html>
```